KVM Contracting services . Building and maintenance services, optic fibre installation

Business cards and logo design.I need a logo that I can use on business cards ,workwear and on my vehicles. I would like the KVM to be the main or larger text and contracting services to be the smaller or less important text.I like monograms, modern designs and repeating patterns symbols. I am also a Gemini and my favourite number is 22 so if this can be any inspiration to help with the design. Am thinking of the using German flag colours as a his is my family’s heritage. And the other 2 main colours I wear is black and white.But any ideas are appreciated.I do not need a design that is trade specific but a design that could be used for any business.

Target Market(s)

General public

Contact Information for Business Card

KVM Contracting Services ( front of business card)

(Back of business card)
Marcus Dellwood
0419274530
Maintenance services
Optic fibre and data installation

Logo Text

Logo can just be pattern or monogram or incorporate KVM . I like the gemini star sign and the number 22

Colors
ec1f27
000000
fbee3e
ffffff

Requirements
Must have
• Logo and KVM Contracting Services on the front of business card
Nice to have
• Possible use of German flag colours.
• Modern design.
• Design to be able to be used on black or white background as I want to put it on clothing

```html
<!DOCTYPE html>
<html lang="en">
<head>
<meta charset="utf-8">
<title>KVM Contracting Services – Business Cards</title>
<link rel="stylesheet" href="https://fonts.googleapis.com/css2?family=Lato:wght@400;700&display=swap">
<style>
  :root {
    --backdrop: #1c1c1c;
    --card: #0f0f0f;
    --card-edge: #262626;
    --ink-bright: #e6e6e6;
    --ink-soft: #b4b4b4;
    --ink-muted: #6e6e6e;
    --rule: #4a4a4a;
  }
  * { margin: 0; padding: 0; box-sizing: border-box; }
  html, body { width: 1200px; height: 900px; overflow: hidden; }
  body {
    background: var(--backdrop);
    font-family: "Lato", sans-serif;
    position: relative;
  }
  .card {
    position: absolute;
    left: 320px;
    width: 560px;
    height: 320px;
    background: linear-gradient(135deg, #161616 0%, var(--card) 55%, #181818 100%);
    border: 1px solid var(--card-edge);
    box-shadow: 0 14px 30px rgba(0,0,0,0.55);
  }
  .card--front { top: 90px; }
  .card--back { top: 470px; }

  /* front */
  .front-brand {
    position: absolute;
    top: 78px; left: 0; right: 0;
    text-align: center;
  }
  .brand-name {
    font-family: "Lato", sans-serif;
    font-weight: 700;
    color: var(--ink-soft);
    line-height: 1;
    display: inline-flex;
    align-items: center;
    gap: 12px;
  }
  .brand-mark {
    width: 16px; height: 16px;
    background: var(--ink-soft);
    display: inline-block;
  }
  .front-brand .brand-name { font-size: 64px; }
  .front-brand .brand-tagline {
    display: block;
    margin-top: 10px;
    font-size: 20px;
    font-weight: 700;
    letter-spacing: 1px;
    color: var(--ink-soft);
    text-transform: uppercase;
  }
  .front-services {
    position: absolute;
    top: 222px; left: 0; right: 0;
    text-align: center;
    font-size: 15px;
    letter-spacing: 2px;
    line-height: 1.5;
    color: var(--ink-muted);
    text-transform: uppercase;
  }

  /* back */
  .back-brand {
    position: absolute;
    left: 34px; top: 112px;
    width: 250px;
    text-align: center;
  }
  .back-brand .brand-name { font-size: 54px; color: var(--ink-muted); }
  .back-brand .brand-mark { background: var(--ink-muted); width: 14px; height: 14px; }
  .back-brand .brand-tagline {
    display: block;
    margin-top: 8px;
    font-size: 16px;
    font-weight: 700;
    color: var(--ink-muted);
    text-transform: uppercase;
    letter-spacing: 0.5px;
  }
  .divider {
    position: absolute;
    left: 305px; top: 60px;
    width: 1px; height: 190px;
    background: var(--rule);
  }
  .contact {
    position: absolute;
    left: 330px; top: 60px;
    color: var(--ink-soft);
  }
  .contact-name {
    font-size: 22px;
    letter-spacing: 1px;
    color: var(--ink-bright);
    text-transform: uppercase;
    font-weight: 400;
  }
  .contact-role { font-size: 14px; color: var(--ink-muted); margin-bottom: 12px; }
  .contact-address { font-size: 15px; line-height: 1.3; margin-bottom: 8px; font-style: normal; }
  .contact-list { list-style: none; font-size: 15px; line-height: 1.45; }
  .contact-list li { display: flex; align-items: center; gap: 9px; }
  .contact-list svg { width: 11px; height: 11px; fill: none; stroke: var(--ink-muted); stroke-width: 1.6; flex: none; }
</style>
</head>
<body>
  <section class="card card--front" aria-label="Card front">
    <div class="front-brand">
      <span class="brand-name"><span class="brand-mark"></span>KVM</span>
      <span class="brand-tagline">Contracting Services</span>
    </div>
    <p class="front-services">Maintenance Services<br>Optic Fibre and Data Installation</p>
  </section>

  <section class="card card--back" aria-label="Card back">
    <div class="back-brand">
      <span class="brand-name"><span class="brand-mark"></span>KVM</span>
      <span class="brand-tagline">Contracting Services</span>
    </div>
    <div class="divider"></div>
    <div class="contact">
      <h1 class="contact-name">Marcus Dellwood</h1>
      <p class="contact-role">Director</p>
      <address class="contact-address">718 Harlow Street,<br>Brookvale, FL 32190, USA</address>
      <ul class="contact-list">
        <li><svg viewBox="0 0 12 12"><path d="M2 1.5h2.5l1 2.5-1.4 1a6 6 0 0 0 2.9 2.9l1-1.4 2.5 1V10.5A1 1 0 0 1 9.5 11.5 8.5 8.5 0 0 1 .5 2.5a1 1 0 0 1 1.5-1z"/></svg>0419274530</li>
        <li><svg viewBox="0 0 12 12"><rect x="1" y="2.5" width="10" height="7"/><path d="M1 2.5l5 4 5-4"/></svg>KVM@kvmcontractingco.com</li>
        <li><svg viewBox="0 0 12 12"><circle cx="6" cy="6" r="5"/><path d="M1 6h10M6 1c2.2 2.6 2.2 7.4 0 10M6 1c-2.2 2.6-2.2 7.4 0 10"/></svg>www.kvmcontractingco.com</li>
      </ul>
    </div>
  </section>
</body>
</html>
```